Website for new dental office

I am Dr. Calvin Merrow and am building a new dental practice. I specialize in general dentistry. I am young and have a higher end dental practice incorporating very new technologies and would like my website to reflect that. As many dental patients are older, the website must be very easy to navigate. I would like patients to be able to request appointments, and will eventually add on patient information forms (the health history, etc, that you normally fill out in the practice) from my practice management software, so leave an area for that.

Industry/Entity Type

Building

```html
<!DOCTYPE html>
<html lang="en">
<head>
<meta charset="utf-8">
<title>Merrow Dental Clinic</title>
<link href="https://fonts.googleapis.com/css2?family=Open+Sans:ital,wght@0,300;0,400;0,600;1,400&display=swap" rel="stylesheet">
<style>
:root{
  --slate:#66889d;
  --slate-dark:#55768b;
  --slate-text:#5c7d92;
  --ink:#333;
  --body:#555;
  --line:#c9d3da;
  --band:#eef1f3;
  --white:#fff;
}
*{box-sizing:border-box;margin:0;padding:0}
html,body{width:971px;height:1200px;overflow:hidden;background:var(--white)}
body{position:relative;font-family:"Open Sans",Arial,sans-serif;color:var(--ink)}
.abs{position:absolute}
.brand{display:flex;align-items:center;gap:8px}
.brand-dot{width:26px;height:26px;border-radius:50%;background:var(--slate)}
.brand-name{font-size:17px;font-weight:400;color:var(--slate-text);line-height:1.1}
.brand-tag{font-size:9px;color:#777;font-family:Arial,sans-serif}
.site-header{top:0;left:0;width:971px;height:58px}
.social{right:138px;top:17px;display:flex;align-items:center;gap:6px;font-size:10px;color:var(--slate-text)}
.social .circle{width:23px;height:23px;border-radius:50%;background:var(--slate)}
.main-nav{top:58px;left:0;width:971px;height:60px;background:var(--slate);color:var(--white)}
.doctor{left:139px;top:10px}
.doctor-name{font-size:17px;font-weight:400}
.doctor-tag{font-size:10px;font-style:italic;margin-top:2px}
.menu{left:342px;top:0;display:flex;height:60px;font-size:11.5px}
.menu a{color:var(--white);text-decoration:none;display:flex;align-items:center;padding:0 17px}
.menu a.active{background:var(--slate-dark);padding:0 21px}
.hero-photo{left:139px;top:138px;width:479px;height:292px;background:linear-gradient(90deg,#f6f1ee 0%,#efe2d8 45%,#e9d2c2 70%,#f3ece7 100%)}
.hero-copy{left:139px;top:170px}
.hero-copy h1{font-size:22px;font-weight:300;color:var(--slate-text)}
.hero-copy .caps{font-size:11.5px;font-weight:600;color:var(--slate-text);margin-top:6px;margin-left:1px}
.hero-copy .lead{font-size:11.5px;color:#555;margin-top:2px;margin-left:1px}
.slider-arrows{left:564px;top:400px;display:flex;gap:2px}
.slider-arrows span{width:18px;height:18px;background:var(--slate);display:flex;align-items:center;justify-content:center}
.appointment{left:618px;top:138px;width:215px;height:292px;background:var(--slate);color:var(--white);padding:20px 24px}
.appointment h2{font-size:24px;font-weight:400;line-height:1.3}
.appointment h3{font-size:15px;font-weight:300;margin:4px 0 10px}
.field{height:24px;border:1px solid #e3eaef;font-size:9.5px;padding:4px 9px;margin-bottom:8px}
.field-row{display:flex;gap:9px}
.field-row .field{flex:1}
.submit{height:32px;background:var(--slate-dark);font:600 9.5px Arial,sans-serif;display:flex;align-items:center;justify-content:center;gap:5px;margin-top:2px}
.welcome{left:0;top:452px;width:971px;text-align:center}
.welcome h2{font-size:24px;font-weight:300;color:var(--slate-text)}
.welcome .intro{font:11.5px Arial,sans-serif;color:#111;margin-top:11px}
.welcome .copy{font:9.5px/20px Arial,sans-serif;color:var(--body);margin-top:8px}
.btn{display:inline-flex;align-items:center;justify-content:center;gap:5px;border:1px solid var(--slate);color:var(--slate-text);font:600 9.5px Arial,sans-serif}
.more{position:absolute;left:384px;top:575px;width:203px;height:38px}
.feature{top:648px;width:213px}
.feature h3{font-size:19px;font-weight:300;color:var(--slate-text);margin-left:-2px}
.feature .photo{height:116px;margin-top:10px}
.feature p{font:8.5px/16px Arial,sans-serif;color:var(--body);margin-top:12px}
.feature .btn{width:91px;height:28px;margin-top:12px;font-size:9px}
.clients{left:0;top:938px;width:971px;height:184px;background:var(--band);border-top:1px solid #e2e6e9}
.clients h2{position:absolute;left:0;width:971px;top:20px;text-align:center;font-size:19px;font-weight:300;color:var(--slate-text)}
.client-nav{right:139px;top:26px;font-size:11px;color:var(--slate-text);letter-spacing:4px}
.testimonial{top:71px;display:flex;gap:18px}
.avatar{width:77px;height:77px;border-radius:50%;flex:none}
.testimonial .name{font:10px Arial,sans-serif;color:var(--slate-text);margin-top:9px}
.testimonial .meta{font:italic 7.5px Arial,sans-serif;color:var(--slate-text);margin-top:5px}
.testimonial p{font:8.5px/16px Arial,sans-serif;color:var(--body);margin-top:8px;width:240px}
.client-divider{left:482px;top:82px;width:1px;height:60px;background:#cfd6db}
.site-footer{left:0;top:1122px;width:971px;height:78px;background:#648599;color:var(--white)}
.site-footer .brand{position:absolute;left:140px;top:22px}
.site-footer .brand-dot{background:var(--white)}
.site-footer .brand-name{color:var(--white)}
.site-footer .brand-tag{color:var(--white)}
.footer-divider{left:342px;top:23px;width:1px;height:36px;background:#c4d1d9}
.footer-links{left:369px;top:21px;display:flex;gap:35px;font-size:9px}
.copyright{left:369px;top:44px;font-size:9px}
</style>
</head>
<body>

<header class="site-header abs">
  <div class="brand abs" style="left:140px;top:12px">
    <span class="brand-dot"></span>
    <div><div class="brand-name">Merrow Dental Clinic</div><div class="brand-tag">specialised in general dentistry</div></div>
  </div>
  <div class="social abs">Follow us :
    <span class="circle" aria-label="Social link"></span><span class="circle" aria-label="Social link"></span><span class="circle" aria-label="Social link"></span><span class="circle" aria-label="Social link"></span><span class="circle" aria-label="Social link"></span>
  </div>
</header>

<nav class="main-nav abs">
  <div class="doctor abs"><div class="doctor-name">Dr. Calvin Merrow</div><div class="doctor-tag">is specialised in general dentistry</div></div>
  <div class="menu abs">
    <a class="active">Home</a><a>About us</a><a>Services</a><a>specialised</a><a>Appointment</a><a>Conatct us</a>
  </div>
</nav>

<div class="hero-photo abs" role="img" aria-label="Smiling patient beside a dental model held in a gloved hand"></div>
<div class="hero-copy abs">
  <h1>Merrow Dental Clinic</h1>
  <div class="caps">DR. CALVIN MERROW IS</div>
  <div class="lead">specialised in general dentistry</div>
</div>
<div class="slider-arrows abs">
  <span><svg width="8" height="10" viewBox="0 0 8 10"><path d="M6 1L2 5l4 4" stroke="#fff" fill="none" stroke-width="1.2"/></svg></span>
  <span><svg width="8" height="10" viewBox="0 0 8 10"><path d="M2 1l4 4-4 4" stroke="#fff" fill="none" stroke-width="1.2"/></svg></span>
</div>

<form class="appointment abs">
  <h2>Merrow<br>Dental Clinic</h2>
  <h3>Request Appointment</h3>
  <div class="field">Name :</div>
  <div class="field">Email :</div>
  <div class="field">Phone :</div>
  <div class="field-row"><div class="field">Date :</div><div class="field">Time :</div></div>
  <div class="submit">SUBMIT NOW <svg width="10" height="9" viewBox="0 0 10 9"><path d="M1 1l3.5 3.5L1 8M5 1l3.5 3.5L5 8" stroke="#fff" fill="none" stroke-width="1.4"/></svg></div>
</form>

<section class="welcome abs">
  <h2>Welcome to Merrow Dental Clinic</h2>
  <p class="intro">He provides higher end dental practice incorporating very new technologies.</p>
  <p class="copy">It is a long established fact that a reader will be distracted by the readable content of a page when looking at its layout. The point of using<br>Lorem Ipsum is that it has a more-or-less normal distribution of letters, as opposed to using 'Content here...</p>
</section>
<div class="btn more">CLICK HERE FOR MORE INFO <svg width="11" height="10" viewBox="0 0 11 10"><path d="M1 1l4 4-4 4M6 1l4 4-4 4" stroke="#5c7d92" fill="none" stroke-width="1.4"/></svg></div>

<article class="feature abs" style="left:139px">
  <h3>Dr. Calvin Merrow</h3>
  <div class="photo" role="img" aria-label="Portrait of the dentist in a white coat" style="background:linear-gradient(90deg,#f4f4f4,#e6ddd6 50%,#f1f1f1)"></div>
  <p>It is a long established fact that a reader will be distracted by the readable content of a page when looking It is a long established fact that a reader...</p>
  <div class="btn">CLICK HERE <svg width="9" height="8" viewBox="0 0 11 10"><path d="M1 1l4 4-4 4M6 1l4 4-4 4" stroke="#5c7d92" fill="none" stroke-width="1.5"/></svg></div>
</article>
<article class="feature abs" style="left:379px">
  <h3>General Dentistry</h3>
  <div class="photo" role="img" aria-label="Dentist examining a patient in the chair" style="background:linear-gradient(90deg,#d9c6bb,#c9d3de 50%,#9fb6c8)"></div>
  <p>It is a long established fact that a reader will be distracted by the readable content of a page when looking It is a long established fact that a reader...</p>
  <div class="btn">CLICK HERE <svg width="9" height="8" viewBox="0 0 11 10"><path d="M1 1l4 4-4 4M6 1l4 4-4 4" stroke="#5c7d92" fill="none" stroke-width="1.5"/></svg></div>
</article>
<article class="feature abs" style="left:620px">
  <h3>Specialised</h3>
  <div class="photo" role="img" aria-label="Dentist in scrubs treating a smiling patient" style="background:linear-gradient(90deg,#3c8c86,#4f9a92 50%,#b7a397)"></div>
  <p>It is a long established fact that a reader will be distracted by the readable content of a page when looking It is a long established fact that a reader...</p>
  <div class="btn">CLICK HERE <svg width="9" height="8" viewBox="0 0 11 10"><path d="M1 1l4 4-4 4M6 1l4 4-4 4" stroke="#5c7d92" fill="none" stroke-width="1.5"/></svg></div>
</article>

<section class="clients abs">
  <h2>Happy Clients</h2>
  <div class="client-nav abs">‹›</div>
  <div class="testimonial abs" style="left:139px">
    <div class="avatar" role="img" aria-label="Photo of a smiling couple" style="background:radial-gradient(circle,#d9b49c,#6b4a38)"></div>
    <div><div class="name">Owen Hartley</div><div class="meta">Journalist &nbsp;&nbsp;|&nbsp;&nbsp; Posted on 25 mar 2014</div><p>It is a long established fact that a reader will be distracted by the readable content of a page when looking...</p></div>
  </div>
  <div class="client-divider abs"></div>
  <div class="testimonial abs" style="left:513px">
    <div class="avatar" role="img" aria-label="Photo of a smiling client" style="background:radial-gradient(circle,#f0d6c6,#8a5a42)"></div>
    <div><div class="name">Owen Hartley</div><div class="meta">Journalist &nbsp;&nbsp;|&nbsp;&nbsp; Posted on 25 mar 2014</div><p>It is a long established fact that a reader will be distracted by the readable content of a page when looking...</p></div>
  </div>
</section>

<footer class="site-footer abs">
  <div class="brand">
    <span class="brand-dot"></span>
    <div><div class="brand-name">Merrow Dental Clinic</div><div class="brand-tag">specialised in general dentistry</div></div>
  </div>
  <div class="footer-divider abs"></div>
  <div class="footer-links abs"><span>Home</span><span>About us</span><span>Services</span><span>Appointment</span><span>Conatct us</span></div>
  <div class="copyright abs">Copyright © 2014. Merrow Dental Clinic. All Rights Reserved</div>
</footer>

</body>
</html>
```